Pelmora needs stationery design

We need desings for presentation cards and letter head for our company. It would be better that the letterhead uses our logo with white background and the presentation card the logo with the black background for the back of the card and the text (name, phone
Updates

Necesitas un par de días antes de escoger al ganador

Colors
0455a3
ec1f27
000000

Requirements
Must have
• Use company logo and colors

```html
<!DOCTYPE html>
<html lang="en">
<head>
<meta charset="utf-8">
<title>Pelmora Business Card</title>
<link rel="stylesheet" href="https://fonts.googleapis.com/css2?family=Oswald:wght@600&family=Quicksand:wght@400;500;700&display=swap">
<style>
  :root {
    --brand-blue: #0455a3;
    --brand-red: #ec1f27;
    --card-black: #1b1b1b;
    --ink-light: #d6d6d6;
    --ink-mid: #9a9a9a;
    --backdrop: #6b6b6b;
  }
  * { margin: 0; padding: 0; box-sizing: border-box; }
  html, body {
    width: 1200px; height: 857px; overflow: hidden;
    background: var(--backdrop);
    font-family: "Quicksand", sans-serif;
  }
  .sheet {
    position: relative; width: 1200px; height: 857px;
    display: flex; align-items: center; justify-content: center; gap: 60px;
  }
  .card {
    position: relative; width: 520px; height: 297px;
    background: var(--card-black);
    border-radius: 3px;
    box-shadow: 0 14px 30px rgba(0,0,0,0.35);
  }
  /* front */
  .card-front { display: flex; align-items: center; justify-content: center; }
  .brand-name {
    display: flex; align-items: center; gap: 14px;
    font-weight: 500; font-size: 54px; letter-spacing: 6px;
    color: var(--ink-mid); text-transform: uppercase;
  }
  .brand-mark { width: 18px; height: 18px; background: var(--brand-red); }
  /* back */
  .identity {
    position: absolute; left: 0; top: 104px; width: 252px;
    text-align: right;
  }
  .person-name {
    font-family: "Oswald", sans-serif; font-weight: 600;
    font-size: 26px; letter-spacing: 1px; color: var(--brand-blue);
    text-transform: uppercase; line-height: 1.1;
  }
  .person-role { font-size: 13px; color: var(--ink-light); margin-top: 4px; }
  .divider {
    position: absolute; left: 268px; top: 96px; width: 2px; height: 66px;
    background: var(--brand-red);
  }
  .contacts {
    position: absolute; left: 288px; top: 96px;
    list-style: none; display: flex; flex-direction: column; gap: 7px;
  }
  .contacts li {
    display: flex; align-items: center; gap: 8px;
    font-size: 13px; color: var(--ink-light);
  }
  .contacts svg { width: 12px; height: 12px; flex: none; }
  .address {
    position: absolute; left: 0; right: 0; bottom: 28px;
    text-align: center; font-size: 12px; color: var(--ink-light);
  }
  .address strong { color: var(--brand-red); font-weight: 700; }
</style>
</head>
<body>
<main class="sheet">
  <section class="card card-front" aria-label="Card front">
    <div class="brand-name"><span class="brand-mark"></span>Pelmora</div>
  </section>

  <section class="card card-back" aria-label="Card back">
    <div class="identity">
      <p class="person-name">Dana Whitfield</p>
      <p class="person-role">Resident Manager</p>
    </div>
    <div class="divider"></div>
    <ul class="contacts">
      <li>
        <svg viewBox="0 0 24 24" fill="#0455a3"><path d="M6.6 10.8a15.1 15.1 0 0 0 6.6 6.6l2.2-2.2a1 1 0 0 1 1-.25 11.4 11.4 0 0 0 3.6.57 1 1 0 0 1 1 1V20a1 1 0 0 1-1 1A17 17 0 0 1 3 4a1 1 0 0 1 1-1h3.5a1 1 0 0 1 1 1c0 1.25.2 2.45.57 3.6a1 1 0 0 1-.25 1z"/></svg>
        +809 555 0142
      </li>
      <li>
        <svg viewBox="0 0 24 24" fill="none" stroke="#0455a3" stroke-width="2.4"><rect x="2" y="5" width="20" height="14" rx="1"/><path d="M2 6l10 7 10-7"/></svg>
        info@northbayops.com
      </li>
      <li>
        <svg viewBox="0 0 24 24" fill="none" stroke="#0455a3" stroke-width="2.2"><circle cx="12" cy="12" r="10"/><path d="M2 12h20M12 2c3 3 3 17 0 20M12 2c-3 3-3 17 0 20"/></svg>
        www.northbayops.com
      </li>
    </ul>
    <p class="address"><strong>Pelmora</strong> - 418 Harbor Row, Ste 6B Easton, MD 21601</p>
  </section>
</main>
</body>
</html>
```